Business card for a young aspring actress

My daughter is 18 and just starting out on her profession as an actress. She is a member of the Open Stage Company and has already had some extras work and a featured role in an upcoming Feature film.

She wants/needs a card that she can have to hand to give to those she comes into contact with in the theatre, TV and film industries.

We are thinking that it may be double sided with an impact side including a picture of her and her name etc with the reverse holding contact and other details.

She wants to go by the name Maren Joy Whitcombe.

She has done a little modelling but sees herself as an actress.

She can be seen in this video
http://www.hollybankacademy.example/videos/a3f19c7d5e2b8406c1d9e7f2a4b60835?width=640&height=480

Target Market(s)

Anyone she comes into contact with in theatre TV and film industries.

Industry/Entity Type

Business

Requirements
Nice to have
• She has email and a website www.marenwhitcombe.example She is quite a connected girl

```html
<!DOCTYPE html>
<html lang="en">
<head>
<meta charset="utf-8">
<title>Maren Joy Whitcombe – Business Card</title>
<link rel="stylesheet" href="https://fonts.googleapis.com/css2?family=Pinyon+Script&family=Questrial&display=swap">
<style>
  :root {
    --page-bg: #e6e4e1;
    --card-light: #ffffff;
    --card-mid: #eeeeee;
    --card-dark: #d4d4d4;
    --name-grey: #8a8a8a;
    --contact-ink: #2e2e2e;
    --icon-ink: #555555;
    --portrait-light: #e8e8e8;
    --portrait-mid: #a9a9a9;
    --portrait-dark: #4a4a4a;
  }
  * { margin: 0; padding: 0; box-sizing: border-box; }
  html, body {
    width: 1200px;
    height: 900px;
    overflow: hidden;
    background: var(--page-bg);
  }
  .card {
    position: absolute;
    left: 100px;
    top: 164px;
    width: 1000px;
    height: 572px;
    border-radius: 28px;
    overflow: hidden;
    background: linear-gradient(160deg, var(--card-light) 0%, var(--card-mid) 55%, var(--card-dark) 100%);
    box-shadow: 0 12px 30px rgba(0, 0, 0, 0.18);
  }
  .portrait {
    position: absolute;
    left: 0;
    top: 0;
    width: 460px;
    height: 100%;
    background:
      radial-gradient(ellipse 45% 40% at 40% 52%, var(--portrait-light) 0%, rgba(232,232,232,0) 100%),
      linear-gradient(90deg, var(--portrait-dark) 0%, var(--portrait-mid) 25%, var(--portrait-light) 60%, rgba(238,238,238,0) 100%);
    -webkit-mask-image: linear-gradient(90deg, #000 55%, transparent 100%);
    mask-image: linear-gradient(90deg, #000 55%, transparent 100%);
  }
  .name {
    position: absolute;
    left: 370px;
    top: 60px;
    font-family: "Pinyon Script", cursive;
    font-weight: 400;
    font-size: 100px;
    line-height: 1.1;
    color: var(--name-grey);
  }
  .name span { display: block; }
  .name .surname { padding-left: 12px; }
  .contacts {
    position: absolute;
    left: 530px;
    top: 310px;
    list-style: none;
    font-family: "Questrial", sans-serif;
    font-size: 21px;
    color: var(--contact-ink);
  }
  .contacts li {
    display: flex;
    align-items: center;
    height: 44px;
  }
  .contacts svg {
    width: 22px;
    height: 22px;
    margin-right: 22px;
    stroke: var(--icon-ink);
    fill: none;
    stroke-width: 1.4;
  }
</style>
</head>
<body>
  <div class="card">
    <div class="portrait" role="img" aria-label="Black and white portrait photo of the actress resting her face on her hands"></div>
    <h1 class="name">
      <span class="given">Maren Joy</span>
      <span class="surname">Whitcombe</span>
    </h1>
    <ul class="contacts">
      <li>
        <svg viewBox="0 0 24 24" aria-hidden="true"><rect x="7" y="3" width="10" height="18" rx="2"/><line x1="10" y1="18" x2="14" y2="18"/></svg>
        000 1234 5678 9000
      </li>
      <li>
        <svg viewBox="0 0 24 24" aria-hidden="true"><rect x="3" y="6" width="18" height="12"/><polyline points="3,6 12,13 21,6"/></svg>
        marenwhitcombe@mail.example
      </li>
      <li>
        <svg viewBox="0 0 24 24" aria-hidden="true"><polyline points="3,12 12,4 21,12"/><polyline points="6,10 6,20 18,20 18,10"/></svg>
        www.marenwhitcombe.example
      </li>
    </ul>
  </div>
</body>
</html>
```